Plakat-Design für Immobilienmakler
Zielgruppe
Wir sind Immobilienmakler und haben eine Geschäftsfläche zu vermieten bekommen. Diese befindet sich an einer viel frequentierten Lage und die Glasflächen sollen beklebt werden.
Aufgabenstellung
Text: Geschäftsfläche mit ca. 200 m2 ab sofort zu vermieten
Hintergrund weiß
Beispielplakate von anderen Objekten sind im Dateianhang
Maße ebenfalls lt. Bild im Anhang
Auf diesem neuen Design soll nur der eine Makler sein von dem das Bild hochgeladen wird.
Die anderen sind nur Beispieldesigns.

```html
<!DOCTYPE html>
<html lang="de">
<head>
<meta charset="utf-8">
<title>Geschäftsfläche zu vermieten – Hausmeridian</title>
<link href="https://fonts.googleapis.com/css2?family=Inter:wght@400;500;700;800&display=swap" rel="stylesheet">
<style>
  :root {
    --stage: #e2e2e2;
    --panel: #ffffff;
    --ink: #111111;
    --box: #0c0c0c;
    --box-text: #ffffff;
    --brand: #1b7a32;
    --photo-top: #f4f5f7;
    --photo-bottom: #dfe3ea;
  }
  html, body {
    margin: 0;
    padding: 0;
    width: 1200px;
    height: 560px;
    overflow: hidden;
    background: var(--stage);
    font-family: "Inter", Arial, sans-serif;
  }
  .canvas {
    position: relative;
    width: 1200px;
    height: 560px;
  }
  .panel {
    position: absolute;
    top: 40px;
    width: 554px;
    height: 481px;
    background: var(--panel);
    box-shadow: 0 3px 8px rgba(0,0,0,0.18);
    overflow: hidden;
  }
  .panel--offer { left: 37px; }
  .panel--brand {
    left: 604px;
    display: flex;
    align-items: center;
    justify-content: center;
  }
  .agent-photo {
    position: absolute;
    left: 0;
    top: 26px;
    width: 200px;
    height: 455px;
    background: linear-gradient(180deg, var(--photo-top), var(--photo-bottom));
  }
  .headline {
    position: absolute;
    right: 22px;
    top: 90px;
    margin: 0;
    text-align: right;
    font-size: 31px;
    line-height: 37px;
    font-weight: 400;
    color: var(--ink);
  }
  .headline strong { font-weight: 700; }
  .contact {
    position: absolute;
    display: flex;
    align-items: center;
    gap: 22px;
    background: var(--box);
    color: var(--box-text);
    font-size: 32px;
    font-weight: 500;
    box-sizing: border-box;
    padding-left: 24px;
    white-space: nowrap;
  }
  .contact--phone { left: 187px; top: 303px; width: 344px; height: 68px; }
  .contact--web { left: 37px; top: 385px; width: 494px; height: 70px; }
  .contact svg { width: 34px; height: 34px; flex: none; }
  .brand-name {
    margin: 0 0 10px;
    font-size: 66px;
    font-weight: 800;
    letter-spacing: -1px;
    color: var(--brand);
  }
</style>
</head>
<body>
<div class="canvas">
  <section class="panel panel--offer">
    <div class="agent-photo" role="img" aria-label="Porträt des Maklers im weißen Hemd"></div>
    <h1 class="headline">Geschäftsfläche<br>mit ca. 200m² ab sofort<br><strong>zu vermieten</strong></h1>
    <div class="contact contact--phone">
      <svg viewBox="0 0 24 24" aria-hidden="true"><path fill="#fff" d="M6.6 10.8c1.4 2.8 3.8 5.1 6.6 6.6l2.2-2.2c.3-.3.7-.4 1-.2 1.1.4 2.3.6 3.6.6.6 0 1 .4 1 1V20c0 .6-.4 1-1 1C10.6 21 3 13.4 3 4c0-.6.4-1 1-1h3.5c.6 0 1 .4 1 1 0 1.3.2 2.5.6 3.6.1.3 0 .7-.2 1z"/></svg>
      <span>0471 238 65 04</span>
    </div>
    <div class="contact contact--web">
      <svg viewBox="0 0 24 24" aria-hidden="true" fill="none" stroke="#fff" stroke-width="2"><circle cx="12" cy="12" r="9"/><path d="M3 12h18M12 3c2.5 2.6 3.8 5.6 3.8 9s-1.3 6.4-3.8 9c-2.5-2.6-3.8-5.6-3.8-9S9.5 5.6 12 3z"/></svg>
      <span>www.hausmeridian.de</span>
    </div>
  </section>
  <section class="panel panel--brand">
    <p class="brand-name">Hausmeridian</p>
  </section>
</div>
</body>
</html>
```